Cash Back to Home Buyers Flyer

We need a flyer for TQ Discount real estate brokerage advertising Money Saving Offer to Home buyers - Cash Back Rebate and explaining how the concept works. The design should communicate how that money saving offer works and should motivate buyers to take advantage of it. Feel free to edit the text based on the attached designs and use infographics.

Target Market(s)

Middle aged professionals

Industry/Entity Type

Real Estate

Requirements
Must have
• Call to action highlights, Dollar signs. Graphics to show rebate math as in the attached file.

```html
<!DOCTYPE html>
<html lang="en">
<head>
<meta charset="utf-8">
<title>TQ Discount – Buyer Rebate Program Flyer</title>
<link href="https://fonts.googleapis.com/css2?family=Poppins:wght@400;600;700&family=Old+Standard+TT:wght@400;700&family=Alfa+Slab+One&family=Bungee+Inline&display=swap" rel="stylesheet">
<style>
  :root{
    --bg:#dcefed;
    --paper:#f4f2ea;
    --cert-cream:#f1efdc;
    --green:#6cbf4a;
    --green-dark:#3d7f2c;
    --band:#2f3a2c;
    --teal:#1fb69b;
    --teal-dark:#15997f;
    --orange:#ec6a2c;
    --ink:#2a2d2c;
    --white:#ffffff;
  }
  *{box-sizing:border-box;margin:0;padding:0}
  html,body{width:1200px;height:936px;overflow:hidden;background:var(--bg)}
  body{font-family:"Poppins",sans-serif;color:var(--ink);position:relative}

  .flyer{position:absolute;left:280px;top:18px;width:640px;height:900px;background:var(--paper);overflow:hidden;box-shadow:0 6px 24px rgba(40,80,75,.18)}

  /* certificate header */
  .certificate{position:absolute;left:14px;top:14px;width:612px;height:318px;
    background:linear-gradient(135deg,#4f9f35,#a6dc7a 30%,#e4f2cf 50%,#a6dc7a 70%,#4f9f35)}
  .certificate-inner{position:absolute;left:40px;top:30px;right:40px;bottom:30px;background:var(--cert-cream);border:2px solid var(--green-dark)}
  .cert-band{position:absolute;left:60px;right:60px;height:24px;background:var(--band);color:#f1efdc;
    font-family:"Alfa Slab One",serif;font-size:12px;letter-spacing:1.5px;text-align:center;line-height:24px;text-transform:uppercase}
  .cert-band.top{top:-12px}
  .cert-band.bottom{bottom:-12px}
  .cert-dollar{position:absolute;width:46px;height:38px;background:var(--band);color:#f1efdc;font-family:"Alfa Slab One",serif;
    font-size:24px;display:flex;align-items:center;justify-content:center;border:2px solid var(--green)}
  .cert-dollar.right{right:-24px;top:60px}
  .cert-dollar.left{left:-24px;bottom:30px}
  .skyline{position:absolute;left:80px;right:80px;top:22px;height:54px;
    background:linear-gradient(180deg,#9fd57d,#6cbf4a)}
  .title{position:absolute;left:0;right:0;top:82px;text-align:center;font-family:"Bungee Inline",sans-serif;
    color:var(--green);line-height:1;text-shadow:2px 2px 0 #cfe7bd}
  .title span{display:block}
  .title .l1{font-size:52px}
  .title .l2{font-size:48px;margin-top:2px}
  .ribbon{position:absolute;left:70px;right:70px;top:196px;height:28px;background:var(--orange);color:var(--white);
    font-family:"Old Standard TT",serif;font-weight:700;font-size:14px;text-align:center;line-height:28px;white-space:nowrap;
    clip-path:polygon(4% 0,100% 0,96% 50%,100% 100%,0 100%,4% 50%,0 0)}
  .cert-url{position:absolute;left:0;right:0;top:230px;text-align:center;font-family:"Old Standard TT",serif;font-size:12px;color:var(--band)}

  .burst{position:absolute;width:96px;height:96px;background:var(--orange);color:var(--white);text-align:center;
    font-weight:700;line-height:1.05;display:flex;flex-direction:column;align-items:center;justify-content:center;
    clip-path:polygon(50% 0,59% 12%,73% 5%,76% 20%,91% 18%,86% 33%,100% 40%,89% 50%,100% 60%,86% 67%,91% 82%,76% 80%,73% 95%,59% 88%,50% 100%,41% 88%,27% 95%,24% 80%,9% 82%,14% 67%,0 60%,11% 50%,0 40%,14% 33%,9% 18%,24% 20%,27% 5%,41% 12%)}
  .burst.left{left:6px;top:150px;font-size:15px;transform:rotate(-28deg)}
  .burst.right{right:8px;top:6px;font-size:13px;transform:rotate(-20deg)}
  .burst .big{font-size:26px}
  .burst .tiny{font-size:8px;font-weight:400}

  /* intro */
  .headline{position:absolute;left:30px;right:30px;top:352px;display:flex;align-items:center;gap:12px;
    font-weight:700;font-size:26px;letter-spacing:.3px;white-space:nowrap}
  .headline::before,.headline::after{content:"";flex:1;height:2px;background:var(--green)}
  .lede{position:absolute;left:40px;right:40px;top:394px;text-align:center;font-family:"Old Standard TT",serif;
    color:var(--orange);font-size:15px;line-height:1.35}
  .lede b{font-weight:700}
  .body-copy{position:absolute;left:60px;right:60px;top:446px;text-align:center;font-size:12.5px;line-height:1.55}
  .body-copy b{font-weight:700}
  .example-banner{position:absolute;left:46px;right:46px;top:530px;background:var(--teal);color:var(--white);
    border-radius:6px;text-align:center;font-size:10.5px;line-height:1.4;padding:6px 8px;white-space:nowrap}
  .example-banner::after{content:"";position:absolute;left:50%;bottom:-9px;margin-left:-9px;border:9px solid transparent;border-bottom:0;border-top-color:var(--teal)}

  /* rebate flow */
  .step{position:absolute;background:var(--teal);color:var(--white);border-radius:6px;font-size:11px;line-height:1.3;
    display:flex;align-items:center;gap:8px;padding:6px 10px;white-space:nowrap}
  .step b{font-weight:700}
  .money-icon{width:24px;height:18px;border-radius:3px;background:linear-gradient(135deg,#8bc96b,#e7b98a);flex:none}
  .house-art{position:absolute;left:40px;top:600px;width:54px;height:48px;border-radius:6px;background:linear-gradient(180deg,#d94b3c,#6cbf4a)}
  .coin{position:absolute;left:52px;top:674px;width:44px;height:44px;border-radius:50%;background:var(--green);border:3px solid var(--white);
    color:var(--white);font-weight:700;font-size:15px;display:flex;align-items:center;justify-content:center;box-shadow:0 0 0 2px var(--green)}
  .savings{position:absolute;left:470px;top:664px;width:160px;height:54px;border:2px dashed var(--teal);border-radius:8px;padding:3px}
  .savings-inner{width:100%;height:100%;background:var(--teal);color:var(--white);border-radius:5px;padding-left:40px;
    display:flex;flex-direction:column;justify-content:center;font-size:10px;line-height:1.2;white-space:nowrap}
  .savings-inner b{font-size:12px}
  .piggy-art{position:absolute;left:454px;top:668px;width:46px;height:44px;border-radius:50%;background:linear-gradient(135deg,#f7b3b8,#e98a94)}

  /* footer */
  .brand{position:absolute;right:32px;top:728px;display:flex;align-items:center;gap:8px;font-weight:600;font-size:18px;color:#5a5f5c}
  .brand::before{content:"";width:14px;height:14px;background:var(--teal)}
  .contact{position:absolute;left:434px;top:762px;font-size:11px}
  .contact .phone{display:flex;align-items:center;gap:6px;font-weight:600;font-size:22px;letter-spacing:.3px;line-height:1.2}
  .contact .web{display:flex;align-items:center;gap:6px;margin-top:2px}
  .footer-wave{position:absolute;left:0;bottom:0;width:640px;height:120px}
  .disclaimer{position:absolute;left:40px;bottom:20px;width:300px;color:var(--white);font-size:12px;line-height:1.45}
  .disclaimer b{font-weight:700}
  .disclaimer .loc{display:flex;align-items:center;gap:4px}
</style>
</head>
<body>
<main class="flyer">

  <section class="certificate" role="img" aria-label="Ornate green banknote frame with leaf flourishes">
    <div class="certificate-inner">
      <div class="cert-band top">TQ Discount Real Estate LLC</div>
      <div class="skyline" role="img" aria-label="Green city skyline and houses illustration"></div>
      <h1 class="title"><span class="l1">Buyer Rebate</span><span class="l2">Program</span></h1>
      <div class="ribbon">Earn up to 2% back when you buy with us!</div>
      <p class="cert-url">www.tqdiscounthomes.com</p>
      <div class="cert-band bottom">Buy and Save</div>
      <div class="cert-dollar right">$</div>
      <div class="cert-dollar left">$</div>
    </div>
  </section>
  <div class="burst left">BUY &amp;<br>SAVE!</div>
  <div class="burst right">EARN<span class="tiny">up to</span><span class="big">2%</span>BACK!</div>

  <h2 class="headline">HOME BUYERS REBATE PROGRAM</h2>
  <p class="lede">If you are buying or planning to buy a property in NJ, this information<br>can make a <b>big difference for you.</b></p>
  <p class="body-copy">You can <b>get up to 2% of Selling price</b> back in your pocket at closing. Average rebate we pay for a $500,000 home sale is about $7,500! The same great level of service, professional advice and guidance PLUS a huge check at your closing to cover your closing costs!</p>
  <div class="example-banner">See an example below, for a house sold for $500,000 Buyers could get a rebate of $6,250<br>(based on 2.5% typically earned by Buyer's Broker).</div>

  <svg class="flow-lines" width="640" height="900" style="position:absolute;left:0;top:0" aria-hidden="true">
    <g fill="none" stroke="#ec6a2c" stroke-width="3">
      <path d="M150 646 V664"/>
      <path d="M266 696 H284"/>
      <path d="M274 696 V624 H284"/>
      <path d="M450 624 H460"/>
      <path d="M548 642 V654"/>
    </g>
    <g fill="#ec6a2c">
      <path d="M144 662 L156 662 L150 672Z"/>
      <path d="M282 690 L292 696 L282 702Z"/>
      <path d="M282 618 L292 624 L282 630Z"/>
      <path d="M458 618 L468 624 L458 630Z"/>
      <path d="M542 652 L554 652 L548 662Z"/>
    </g>
  </svg>

  <div class="house-art" role="img" aria-label="Red house illustration on green lawn"></div>
  <div class="step" style="left:100px;top:604px;width:150px">Buyer Purchases<br>Home for $500,000</div>
  <div class="coin">5%</div>
  <div class="step" style="left:104px;top:676px;width:162px">Purchase Price includes<br>5% Commission</div>
  <div class="step" style="left:292px;top:604px;width:158px"><span class="money-icon" role="img" aria-label="Hand holding cash"></span><span>2.5% to Buyer's<br>Broker $12,500</span></div>
  <div class="step" style="left:292px;top:676px;width:158px"><span class="money-icon" role="img" aria-label="Hand holding cash"></span><span>2.5% to Seller's<br>Broker $12,500</span></div>
  <div class="step" style="left:468px;top:604px;width:162px"><span class="money-icon" role="img" aria-label="Hand holding cash"></span><span>Broker pays <b>1.25%</b><br>Rebate to Buyer</span></div>
  <div class="savings"><div class="savings-inner"><span>Buyer's</span><b>SAVINGS $6,250</b></div></div>
  <div class="piggy-art" role="img" aria-label="Pink piggy bank with coins"></div>

  <div class="brand">TQ Discount</div>

  <div class="contact">
    <div class="phone">
      <svg width="16" height="16" viewBox="0 0 24 24" aria-hidden="true"><path fill="#1fb69b" d="M6.6 10.8a15 15 0 0 0 6.6 6.6l2.2-2.2c.3-.3.7-.4 1-.2 1.1.4 2.3.6 3.6.6.6 0 1 .4 1 1V20c0 .6-.4 1-1 1A17 17 0 0 1 3 4c0-.6.4-1 1-1h3.5c.6 0 1 .4 1 1 0 1.3.2 2.5.6 3.6.1.3 0 .7-.2 1z"/></svg>
      555-014-2290
    </div>
    <div class="web">
      <svg width="12" height="12" viewBox="0 0 24 24" aria-hidden="true"><circle cx="12" cy="12" r="10" fill="none" stroke="#1fb69b" stroke-width="2.5"/><path d="M2 12h20M12 2c3 3 3 17 0 20M12 2c-3 3-3 17 0 20" fill="none" stroke="#1fb69b" stroke-width="2"/></svg>
      www.tqbuyerrebate.com
    </div>
  </div>

  <svg class="footer-wave" viewBox="0 0 640 120" aria-hidden="true">
    <defs><linearGradient id="tealFade" x1="0" x2="1"><stop offset="0" stop-color="#5cc39a"/><stop offset="1" stop-color="#16a88c"/></linearGradient></defs>
    <path d="M0 120 V45 C0 12 40 0 120 0 H300 C360 0 380 70 480 78 C560 86 610 70 640 60 V120Z" fill="url(#tealFade)"/>
  </svg>
  <p class="disclaimer">All commissions are <b>negotiable</b> in NJ. Consult a tax professional regarding a receipt of the rebate.
    <span class="loc"><svg width="10" height="12" viewBox="0 0 24 28" aria-hidden="true"><path fill="#fff" d="M12 0a9 9 0 0 0-9 9c0 7 9 19 9 19s9-12 9-19a9 9 0 0 0-9-9zm0 13a4 4 0 1 1 0-8 4 4 0 0 1 0 8z"/></svg>Location: New Jersey</span></p>

</main>
</body>
</html>
```